KIVO 248
I need double sided standard sized Business Card [3.5" x 2"]
Open to designers choice
Modern
Pavel Rudakovsky
PO BOX 7132
Halvern, NV 90318
pavel@tumq4.com
kivo248.com

```html
<!DOCTYPE html>
<html lang="en">
<head>
<meta charset="utf-8">
<title>KIVO 248 — Business Card</title>
<link href="https://fonts.googleapis.com/css2?family=Open+Sans:wght@400;600;700&display=swap" rel="stylesheet">
<style>
  :root {
    --page-bg: #d9d9d9;
    --card-dark-top: #2a211d;
    --card-dark-bottom: #0c0908;
    --card-light: #ffffff;
    --card-light-edge: #ececec;
    --brand-orange: #f0641e;
    --brand-red: #d7271e;
    --band-yellow: #f7b52c;
    --band-orange: #ef5a22;
    --text-dark: #333333;
    --text-muted: #666666;
    --rule: #b5b5b5;
  }
  * { box-sizing: border-box; margin: 0; padding: 0; }
  html, body { width: 1200px; height: 901px; overflow: hidden; }
  body {
    background: var(--page-bg);
    font-family: "Open Sans", Arial, sans-serif;
    display: flex;
    flex-direction: column;
    align-items: center;
    justify-content: center;
    gap: 48px;
  }
  .card {
    width: 640px;
    height: 366px;
    border-radius: 20px;
    position: relative;
    overflow: hidden;
    box-shadow: 0 6px 18px rgba(0,0,0,0.18);
  }

  /* Back side */
  .card-back {
    background: linear-gradient(160deg, var(--card-dark-top), var(--card-dark-bottom) 70%);
    display: flex;
    align-items: center;
    justify-content: center;
  }
  .back-brand {
    display: flex;
    align-items: center;
    gap: 16px;
    margin-top: -20px;
  }
  .brand-square {
    width: 54px;
    height: 54px;
    border-radius: 10px;
    background: linear-gradient(180deg, var(--band-yellow), var(--band-orange));
  }
  .back-brand .brand-name {
    font-size: 44px;
    font-weight: 700;
    color: var(--brand-orange);
    letter-spacing: 1px;
  }
  .back-web {
    position: absolute;
    bottom: 34px;
    width: 100%;
    text-align: center;
    font-size: 13px;
    letter-spacing: 5px;
    color: #6f625c;
  }

  /* Front side */
  .card-front {
    background: linear-gradient(180deg, var(--card-light) 70%, var(--card-light-edge));
  }
  .front-brand {
    position: absolute;
    top: 30px;
    left: 226px;
    display: flex;
    align-items: center;
    gap: 14px;
  }
  .front-brand .brand-square {
    width: 62px;
    height: 62px;
    background: linear-gradient(180deg, #4a4a4a, #1c1c1c);
  }
  .front-brand .brand-name {
    font-size: 40px;
    font-weight: 700;
    color: var(--brand-orange);
    letter-spacing: 1px;
  }
  .holder {
    position: absolute;
    top: 136px;
    right: 362px;
    text-align: right;
  }
  .holder-name {
    font-size: 17px;
    font-weight: 700;
    color: var(--brand-red);
  }
  .holder-title {
    font-size: 12px;
    color: var(--text-muted);
    margin-top: 4px;
  }
  .divider {
    position: absolute;
    top: 134px;
    left: 292px;
    width: 1px;
    height: 118px;
    background: var(--rule);
  }
  .contact {
    position: absolute;
    top: 132px;
    left: 306px;
    font-size: 12px;
    line-height: 16px;
    color: var(--text-dark);
  }
  .contact-list { list-style: none; margin-top: 4px; }
  .contact-list li { display: flex; align-items: center; gap: 8px; height: 16px; }
  .contact-list svg { width: 12px; height: 12px; fill: var(--brand-orange); }
  .band-rule {
    position: absolute;
    left: 0; right: 0;
    bottom: 74px;
    height: 2px;
    background: var(--rule);
  }
  .band {
    position: absolute;
    left: 0; right: 0; bottom: 0;
    height: 66px;
    background: linear-gradient(180deg, var(--band-yellow), var(--band-orange));
    display: flex;
    align-items: flex-end;
    padding: 0 0 12px 96px;
  }
  .band-web {
    font-size: 12px;
    letter-spacing: 6px;
    color: #ffffff;
  }
</style>
</head>
<body>
  <section class="card card-back" aria-label="Business card back">
    <div class="back-brand">
      <span class="brand-square"></span>
      <span class="brand-name">KIVO 248</span>
    </div>
    <div class="back-web">www.kivo248.com</div>
  </section>

  <section class="card card-front" aria-label="Business card front">
    <div class="front-brand">
      <span class="brand-square"></span>
      <span class="brand-name">KIVO 248</span>
    </div>

    <div class="holder">
      <div class="holder-name">Pavel Rudakovsky</div>
      <div class="holder-title">CEO</div>
    </div>

    <div class="divider"></div>

    <div class="contact">
      <div>PO BOX 7132</div>
      <div>Halvern, NV 90318</div>
      <ul class="contact-list">
        <li>
          <svg viewBox="0 0 12 12"><path d="M2.5 0.5 L4.5 0.5 L5.2 3 L3.9 4 C4.5 5.5 6.5 7.5 8 8.1 L9 6.8 L11.5 7.5 L11.5 9.5 C11.5 10.6 10.6 11.5 9.5 11.5 C4.5 11.2 0.8 7.5 0.5 2.5 C0.5 1.4 1.4 0.5 2.5 0.5 Z"/></svg>
          <span>8005550193</span>
        </li>
        <li>
          <svg viewBox="0 0 12 12"><path d="M1 3 C1 1.5 11 1.5 11 3 L11 4.5 L8.5 4.5 L8.5 3.5 L3.5 3.5 L3.5 4.5 L1 4.5 Z M2.5 6 L9.5 6 L10.5 11.5 L1.5 11.5 Z"/></svg>
          <span>3205550148</span>
        </li>
        <li>
          <svg viewBox="0 0 12 12"><path d="M3 0.5 L9 0.5 L9 4 L3 4 Z M1 5 L11 5 L11 10 L9 10 L9 11.5 L3 11.5 L3 10 L1 10 Z"/></svg>
          <span>8005550193</span>
        </li>
        <li>
          <svg viewBox="0 0 12 12"><path d="M0.5 2.5 L11.5 2.5 L11.5 10 L0.5 10 Z M1.5 3.5 L6 7 L10.5 3.5 Z" fill-rule="evenodd"/></svg>
          <span>pavel@tumq4.com</span>
        </li>
      </ul>
    </div>

    <div class="band-rule"></div>
    <div class="band">
      <span class="band-web">www.kivo248.com</span>
    </div>
  </section>
</body>
</html>
```